Business Card 85x40mm - Freelance audio mixing / live event operator

I am a freelance audio operator working in live events. Mostly corporate events mixing sound for a range of entertainment, awards nights and functions. I need a new card to give to perspective clients.

The final design will convey bold professionalism with a general dark vibe. Looking for dark-ish background with some smatterings of colour added.

I have attatched my old BC for an idea of what I have liked in the past. Id like a more modern updated design (that circular design on the back is not my logo it is just a picture I found that resembled sound} . For an added element possibly a mixture of some playful colours in a way that resembles an audio wave form or sound.

I have attached a photo called "audio software" with some colourful squiggly lines; maybe incorporate elements of that into into design
Updates

Added extra $ to project Damn Pixel hives fees are unreasonable

Target Market(s)

Mostly corporate clients

Industry/Entity Type

Events

Contact Information for Business Card

Corwin Pellath
Sound | FOH | Monitors | Systems | Corporate

Digital Audio Mixing Specialist, Live Event Technical Professional,

corwinpellath@mailvexo.net, +61 402 918 357

Colors
ec1f27
ffc214
9bcb3c
6b449b

Requirements
Must have
• Dark theme
• 85x40mm dimensions
Nice to have
• some sort of imagery or design to reflect audio/sound

```html
<!DOCTYPE html>
<html lang="en">
<head>
<meta charset="utf-8">
<title>Corwin Pellath – Business Card</title>
<link rel="stylesheet" href="https://fonts.googleapis.com/css2?family=Lato:wght@300;400;700;900&display=swap">
<style>
  :root {
    --backdrop: #d9d9d9;
    --card: #000000;
    --ink: #ffffff;
    --ink-soft: #e6e6e6;
    --violet: #6b4d8a;
    --red: #ec1f27;
    --orange: #f26a2a;
    --amber: #ffc214;
    --green: #9bcb3c;
    --purple: #6b449b;
  }
  * { margin: 0; padding: 0; box-sizing: border-box; }
  html, body {
    width: 1200px;
    height: 1199px;
    overflow: hidden;
    background: var(--backdrop);
    font-family: "Lato", sans-serif;
  }
  .canvas {
    position: relative;
    width: 1200px;
    height: 1199px;
  }
  .card {
    position: absolute;
    width: 580px;
    height: 330px;
    background: var(--card);
    color: var(--ink);
    box-shadow: 0 18px 40px rgba(0,0,0,0.18);
    overflow: hidden;
  }
  .card-front { left: 560px; top: 240px; }
  .card-back  { left: 60px;  top: 620px; }

  .wave-emblem {
    position: absolute;
    left: 175px;
    top: 58px;
    width: 230px;
    height: 104px;
    border-radius: 14px;
    background: linear-gradient(90deg, var(--orange) 0%, var(--amber) 35%, var(--green) 60%, var(--purple) 100%);
    opacity: 0.85;
  }
  .front-identity {
    position: absolute;
    left: 0; right: 0;
    top: 178px;
    text-align: center;
  }
  .holder-name {
    font-weight: 900;
    font-size: 30px;
    letter-spacing: 0.5px;
    text-transform: uppercase;
    color: var(--ink);
    line-height: 1;
  }
  .service-list {
    margin-top: 20px;
    font-weight: 400;
    font-size: 16px;
    color: var(--ink-soft);
    letter-spacing: 0.2px;
  }

  .back-rule {
    position: absolute;
    left: 0; top: 0;
    width: 580px;
    height: 120px;
  }
  .wave-trail {
    position: absolute;
    left: 408px;
    top: 44px;
    width: 150px;
    height: 62px;
    border-radius: 8px;
    background: linear-gradient(90deg, var(--purple) 0%, #8a7c7a 50%, var(--amber) 100%);
    opacity: 0.85;
  }
  .back-details {
    position: absolute;
    left: 56px;
    top: 170px;
  }
  .role-summary {
    font-weight: 700;
    font-size: 15px;
    line-height: 1.25;
    color: var(--ink);
  }
  .contact-line {
    margin-top: 12px;
    font-weight: 400;
    font-size: 14px;
    color: var(--ink-soft);
  }
</style>
</head>
<body>
<main class="canvas">

  <section class="card card-front" aria-label="Card front">
    <div class="wave-emblem" role="img" aria-label="Colourful audio waveform emblem"></div>
    <div class="front-identity">
      <h1 class="holder-name">Corwin Pellath</h1>
      <p class="service-list">Sound | FOH | Monitors | Systems | Corporate</p>
    </div>
  </section>

  <section class="card card-back" aria-label="Card back">
    <svg class="back-rule" viewBox="0 0 580 120" aria-hidden="true">
      <polyline points="0,18 400,18 400,50 408,50" fill="none" stroke="var(--violet)" stroke-width="3"/>
      <line x1="558" y1="100" x2="580" y2="100" stroke="var(--amber)" stroke-width="3"/>
    </svg>
    <div class="wave-trail" role="img" aria-label="Colourful audio waveform trail"></div>
    <div class="back-details">
      <p class="role-summary">Live Digital Audio Mixing,<br>(*Technical) Events Professional,<br>(*Audio Visual Technician)</p>
      <p class="contact-line">corwinpellath@mailvexo.net // +61 402 918 357</p>
    </div>
  </section>

</main>
</body>
</html>
```